Book a car wash

The app will have a logo, contact details and address
It will then lead you to booking a service from list
The customer will have a date, day and time

Booking - There are two types of times arrival is the main - day, date, time, service, payment. Each car takes and average of 1.5 hours

Pay by qfund or cashlyn or merchant

List of services
Bronze $25
Silver $40
Gold $55
Leather Plus $90
Diamond $100
Ruby $100
Standard Vehicle $0
Larger Vehicle & 4wd $10

Target Market(s)

Professionals with time issues
Parents with time management concerns

Industry/Entity Type

It Service

Requirements
Must have
• Logo
Menu list
Payment system
Address and contact details
Basement CarPark - Winsley Arcade Shopping Centre
Tolvane rd, Claremont
0493527641
Nice to have
• Big fonts and step by step process
Should not have
• No cars or washing items i.e. sponges

```html
<!DOCTYPE html>
<html lang="en">
<head>
<meta charset="utf-8">
<title>Book a Car Wash – Service Selection Screens</title>
<link rel="stylesheet" href="https://fonts.googleapis.com/css2?family=Nunito+Sans:wght@300;400&display=swap">
<style>
  :root {
    --orange: #f9b03e;
    --orange-text: #f6a83a;
    --orange-line: #fbe3bd;
    --white: #ffffff;
    --grey-text: #8c8c8c;
    --dark-text: #3a3a3a;
    --border: #dcdcdc;
    --radio-ring: #ececec;
    --panel-fade: #f1f1f1;
    --bronze: #c4242e;
    --silver: #4a4a4a;
    --gold: #f7941d;
    --leather: #623814;
    --body-text: #6e6e6e;
  }
  * { box-sizing: border-box; margin: 0; padding: 0; }
  html, body { width: 1200px; height: 675px; overflow: hidden; background: var(--white); }
  body { position: relative; font-family: "Nunito Sans", Arial, sans-serif; font-weight: 300; }

  .screen {
    position: absolute; width: 329px; height: 499px;
    border: 1px solid var(--border);
    background: linear-gradient(to bottom, var(--white) 55%, var(--panel-fade) 100%);
    overflow: hidden;
  }
  .screen--plain { left: 22px; top: 91px; }
  .screen--priced { left: 380px; top: 92px; }
  .screen--cards { left: 742px; top: 93px; background: var(--panel-fade); }

  .app-bar {
    position: absolute; left: 0; top: 0; width: 100%; height: 54px;
    background: var(--orange);
  }
  .app-bar__title {
    position: absolute; left: 0; right: 0; top: 0; line-height: 54px;
    text-align: center; color: var(--white); font-size: 21px; font-weight: 400;
  }
  .app-bar__icon { position: absolute; top: 10px; width: 34px; height: 34px; }
  .app-bar__icon--back { left: 11px; }
  .app-bar__icon--settings { right: 11px; }

  .screen__heading {
    position: absolute; left: 0; right: 0; text-align: center;
    color: var(--grey-text); font-size: 18px; font-weight: 300;
  }
  .screen--plain .screen__heading, .screen--priced .screen__heading { top: 96px; }
  .screen--cards .screen__heading { top: 69px; }
  .screen--cards .heading-band {
    position: absolute; left: 0; top: 54px; width: 100%; height: 71px; background: var(--white);
  }

  .service-list { list-style: none; position: absolute; left: 0; top: 149px; width: 100%; }
  .service {
    position: relative; height: 40.4px; display: flex; align-items: center;
    color: var(--orange-text); font-size: 18.5px;
  }
  .service__radio {
    position: absolute; left: 29px; top: 9px; width: 22px; height: 22px; border-radius: 50%;
    border: 2px solid var(--radio-ring); background: var(--white);
  }
  .service--selected .service__radio::after {
    content: ""; position: absolute; left: 4px; top: 4px; width: 10px; height: 10px;
    border-radius: 50%; background: var(--orange);
  }
  .service--selected { color: var(--dark-text); }
  .service__name { position: absolute; left: 63px; }
  .service__price {
    position: absolute; right: 29px; font-size: 15px; color: var(--grey-text);
  }
  .service--selected .service__price { color: var(--dark-text); }
  .screen--priced .service::after {
    content: ""; position: absolute; left: 107px; right: 29px; bottom: 8px;
    height: 1px; background: var(--orange-line);
  }

  .card-list { list-style: none; position: absolute; left: 0; top: 125px; width: 100%; }
  .card {
    position: relative; height: 78px; margin-bottom: 10px; background: var(--white);
  }
  .card__bar { position: absolute; left: 0; top: 0; width: 21px; height: 100%; }
  .card__name { position: absolute; left: 42px; top: 8px; font-size: 18.5px; font-weight: 400; }
  .card__price { position: absolute; right: 16px; top: 11px; font-size: 15px; color: var(--grey-text); }
  .card__text {
    position: absolute; left: 31px; right: 10px; top: 38px;
    font-size: 11px; line-height: 16px; color: var(--body-text); font-weight: 300;
  }
  .card--bronze .card__bar { background: var(--bronze); } .card--bronze .card__name { color: var(--bronze); }
  .card--silver .card__bar { background: var(--silver); } .card--silver .card__name { color: var(--silver); }
  .card--gold .card__bar { background: var(--gold); } .card--gold .card__name { color: var(--gold); }
  .card--leather .card__bar { background: var(--leather); } .card--leather .card__name { color: var(--leather); }
</style>
</head>
<body>

<!-- Step: plain list -->
<section class="screen screen--plain">
  <header class="app-bar">
    <svg class="app-bar__icon app-bar__icon--back" viewBox="0 0 34 34"><circle cx="17" cy="17" r="15" fill="none" stroke="#fff" stroke-width="2.5"/><path d="M25 17H11M17 10l-7 7 7 7" fill="none" stroke="#fff" stroke-width="3" stroke-linecap="round" stroke-linejoin="round"/></svg>
    <h1 class="app-bar__title">Book a Car Wash</h1>
    <svg class="app-bar__icon app-bar__icon--settings" viewBox="0 0 34 34"><circle cx="17" cy="17" r="15" fill="none" stroke="#fff" stroke-width="2.5"/><g fill="#fff"><circle cx="17" cy="17" r="7"/><g stroke="#fff" stroke-width="3.2" stroke-linecap="round"><path d="M17 7v3M17 24v3M7 17h3M24 17h3M10 10l2 2M22 22l2 2M24 10l-2 2M12 22l-2 2"/></g></g><circle cx="17" cy="17" r="3" fill="var(--orange)"/></svg>
  </header>
  <h2 class="screen__heading">Select a service type</h2>
  <ul class="service-list">
    <li class="service"><span class="service__radio"></span><span class="service__name">Bronze</span></li>
    <li class="service"><span class="service__radio"></span><span class="service__name">Silver</span></li>
    <li class="service service--selected"><span class="service__radio"></span><span class="service__name">Gold</span></li>
    <li class="service"><span class="service__radio"></span><span class="service__name">Leather Plus</span></li>
    <li class="service"><span class="service__radio"></span><span class="service__name">Diamond</span></li>
    <li class="service"><span class="service__radio"></span><span class="service__name">Ruby</span></li>
    <li class="service"><span class="service__radio"></span><span class="service__name">Standard Vehicle</span></li>
    <li class="service"><span class="service__radio"></span><span class="service__name">Large Vehicle &amp; 4WD</span></li>
  </ul>
</section>

<!-- Step: list with prices -->
<section class="screen screen--priced">
  <header class="app-bar">
    <svg class="app-bar__icon app-bar__icon--back" viewBox="0 0 34 34"><circle cx="17" cy="17" r="15" fill="none" stroke="#fff" stroke-width="2.5"/><path d="M25 17H11M17 10l-7 7 7 7" fill="none" stroke="#fff" stroke-width="3" stroke-linecap="round" stroke-linejoin="round"/></svg>
    <h1 class="app-bar__title">Book a Car Wash</h1>
    <svg class="app-bar__icon app-bar__icon--settings" viewBox="0 0 34 34"><circle cx="17" cy="17" r="15" fill="none" stroke="#fff" stroke-width="2.5"/><g fill="#fff"><circle cx="17" cy="17" r="7"/><g stroke="#fff" stroke-width="3.2" stroke-linecap="round"><path d="M17 7v3M17 24v3M7 17h3M24 17h3M10 10l2 2M22 22l2 2M24 10l-2 2M12 22l-2 2"/></g></g><circle cx="17" cy="17" r="3" fill="var(--orange)"/></svg>
  </header>
  <h2 class="screen__heading">Select a service type</h2>
  <ul class="service-list">
    <li class="service"><span class="service__radio"></span><span class="service__name">Bronze</span><span class="service__price">$ 25</span></li>
    <li class="service"><span class="service__radio"></span><span class="service__name">Silver</span><span class="service__price">$ 40</span></li>
    <li class="service service--selected"><span class="service__radio"></span><span class="service__name">Gold</span><span class="service__price">$ 55</span></li>
    <li class="service"><span class="service__radio"></span><span class="service__name">Leather Plus</span><span class="service__price">$ 90</span></li>
    <li class="service"><span class="service__radio"></span><span class="service__name">Diamond</span><span class="service__price">$ 100</span></li>
    <li class="service"><span class="service__radio"></span><span class="service__name">Ruby</span><span class="service__price">$ 100</span></li>
    <li class="service"><span class="service__radio"></span><span class="service__name">Standard Vehicle</span><span class="service__price">$ 0</span></li>
    <li class="service"><span class="service__radio"></span><span class="service__name">Large Vehicle &amp; 4WD</span><span class="service__price">$ 10</span></li>
  </ul>
</section>

<!-- Step: service cards -->
<section class="screen screen--cards">
  <header class="app-bar">
    <svg class="app-bar__icon app-bar__icon--back" viewBox="0 0 34 34"><circle cx="17" cy="17" r="15" fill="none" stroke="#fff" stroke-width="2.5"/><path d="M25 17H11M17 10l-7 7 7 7" fill="none" stroke="#fff" stroke-width="3" stroke-linecap="round" stroke-linejoin="round"/></svg>
    <h1 class="app-bar__title">Book a Car Wash</h1>
    <svg class="app-bar__icon app-bar__icon--settings" viewBox="0 0 34 34"><circle cx="17" cy="17" r="15" fill="none" stroke="#fff" stroke-width="2.5"/><g fill="#fff"><circle cx="17" cy="17" r="7"/><g stroke="#fff" stroke-width="3.2" stroke-linecap="round"><path d="M17 7v3M17 24v3M7 17h3M24 17h3M10 10l2 2M22 22l2 2M24 10l-2 2M12 22l-2 2"/></g></g><circle cx="17" cy="17" r="3" fill="var(--orange)"/></svg>
  </header>
  <div class="heading-band"></div>
  <h2 class="screen__heading">Select a service type</h2>
  <ul class="card-list">
    <li class="card card--bronze"><span class="card__bar"></span><span class="card__name">Bronze</span><span class="card__price">$ 25</span><p class="card__text">Lorem ipsum dolor sit amet, consectetur adipisicing elit, sed do eiusmod tempor incididunt ut labore et dolore</p></li>
    <li class="card card--silver"><span class="card__bar"></span><span class="card__name">Silver</span><span class="card__price">$ 40</span><p class="card__text">Lorem ipsum dolor sit amet, consectetur adipisicing elit, sed do eiusmod tempor incididunt ut labore et dolore</p></li>
    <li class="card card--gold"><span class="card__bar"></span><span class="card__name">Gold</span><span class="card__price">$ 55</span><p class="card__text">Lorem ipsum dolor sit amet, consectetur adipisicing elit, sed do eiusmod tempor incididunt ut labore et dolore</p></li>
    <li class="card card--leather"><span class="card__bar"></span><span class="card__name">Leather Plus</span><span class="card__price">$ 90</span><p class="card__text">Lorem ipsum dolor sit amet, consectetur adipisicing elit, sed do eiusmod tempor incididunt ut labore et dolore</p></li>
  </ul>
</section>

</body>
</html>
```